PPC Landing Page - PSD or AI only

Need a landing page to replace harwickdenservices.com

This page will be used for PPC only, so the CTA's and forms need to be very clear. Will have 4 inner landing pages plus 2 content pages.

Pages will be
Household Moves
Corporate Moves
Military Moves
Auto Transport

About Us
Testimonials

Form will be basic, will have the following inputs:
Name
Email
Mobile
Moving from zip:
Moving to zip:
(Drop box) Move type: Residential > Corporate > Auto Transport > Military > Other

Content can be taken from original site. Please do not use Lorem Ipsum

• Optimized for PPC traffic.
• Text logo.

```html
<!DOCTYPE html>
<html lang="en">
<head>
<meta charset="utf-8">
<title>Harwickden Relocation Services – Long Distance Moving</title>
<link href="https://fonts.googleapis.com/css2?family=Open+Sans:ital,wght@0,400;0,600;0,700;0,800;1,700;1,800&display=swap" rel="stylesheet">
<style>
:root{
  --gold:#c59d3a;
  --gold-dark:#a9842a;
  --gold-light:#e0bd62;
  --ink:#2a2a2a;
  --text:#555;
  --muted:#8a8a8a;
  --line:#e1e1e1;
  --wood:#2f2b28;
  --wood-2:#3d3834;
  --footer:#1f1f1f;
  --white:#fff;
  --page:#f3f3f3;
}
*{box-sizing:border-box;margin:0;padding:0}
html,body{width:1200px;height:2512px;overflow:hidden}
body{font-family:"Open Sans",Arial,sans-serif;color:var(--text);background:var(--white);position:relative}

/* header */
.site-header{height:60px;display:flex;align-items:center;justify-content:space-between;padding:0 100px 0 108px;background:var(--white)}
.brand{display:flex;align-items:center;gap:12px}
.brand-dot{width:38px;height:38px;border-radius:50%;background:var(--gold)}
.brand-name{font-size:26px;font-weight:400;color:var(--gold);letter-spacing:.5px;text-transform:uppercase}
.header-call{text-align:right;line-height:1.1}
.header-call small{display:block;font-size:11px;font-weight:700;color:var(--ink);letter-spacing:1px}
.header-call strong{font-size:22px;font-weight:800;color:var(--ink)}
.header-call svg{vertical-align:-3px;margin-right:6px}

.main-nav{height:26px;background:var(--gold);display:flex;justify-content:center;gap:0}
.main-nav a{color:var(--white);text-decoration:none;font-size:11px;font-weight:700;text-transform:uppercase;padding:0 18px;line-height:26px}
.main-nav a.active{background:var(--gold-dark)}

/* hero */
.hero{position:relative;height:520px;background:linear-gradient(100deg,#d9c7a6 0%,#cdb48c 40%,#b99970 70%,#8c6c4a 100%)}
.hero-photo{position:absolute;inset:0}
.hero-box{position:absolute;left:130px;top:60px;width:350px;padding:24px 22px 22px;background:rgba(255,255,255,.55)}
.hero-box h1{font-size:34px;line-height:1.15;font-style:italic;font-weight:800;color:var(--white);text-shadow:0 1px 2px rgba(0,0,0,.2);margin-bottom:14px}
.hero-box p{font-size:15px;line-height:1.45;color:var(--white);margin-bottom:20px}
.btn{display:inline-block;background:var(--gold);color:var(--white);font-weight:700;text-transform:uppercase;text-decoration:none}
.hero-box .btn{font-size:13px;padding:13px 16px}
.hero-dots{position:absolute;left:130px;top:476px;display:flex;gap:8px}
.hero-dots span{width:12px;height:12px;border-radius:50%;background:rgba(255,255,255,.6)}
.hero-dots span.on{background:var(--white)}

/* service cards */
.services{display:flex;justify-content:center;gap:28px;padding:40px 0}
.service-card{width:472px;height:214px;border:1px solid var(--line);display:flex;align-items:center;padding:0 24px;gap:20px;background:var(--white)}
.service-card.reverse{flex-direction:row-reverse}
.service-img{width:160px;height:120px;flex:none}
.service-card h2{font-size:20px;font-weight:700;color:var(--ink);margin-bottom:8px}
.service-card p{font-size:13px;line-height:1.5;color:var(--text)}

/* quote form */
.quote{height:440px;background:repeating-linear-gradient(90deg,var(--wood) 0 60px,var(--wood-2) 60px 62px,var(--wood) 62px 140px);padding-top:44px;color:var(--white)}
.quote h2{font-size:26px;font-weight:700;text-align:center;text-transform:uppercase;letter-spacing:.5px}
.quote-divider{width:1200px;height:1px;background:rgba(255,255,255,.25);margin:14px 0 16px}
.quote-lead{text-align:center;font-size:16px;font-weight:600;margin-bottom:40px}
.quote-form{width:920px;margin:0 auto;display:grid;grid-template-columns:1fr 1fr;column-gap:36px}
.field{margin-bottom:10px}
.field label{display:block;font-size:12px;margin-bottom:4px}
.field .input{height:24px;background:var(--white);border:1px solid #ccc}
.field .select{height:24px;background:var(--white);border:1px solid #ccc;font-size:12px;color:var(--ink);padding:3px 8px;display:flex;justify-content:space-between}
.quote-form .btn{width:100%;height:40px;font-size:22px;line-height:40px;text-align:center;margin-top:6px}

/* about */
.about{display:flex;justify-content:space-between;padding:50px 130px 0 130px;height:360px}
.about-text{width:560px}
.about-title{display:flex;align-items:center;gap:10px;margin-bottom:16px}
.about-title .mark{width:30px;height:30px;border-radius:50%;background:var(--gold)}
.about-title h2{font-size:20px;font-weight:700;color:var(--ink);text-transform:uppercase}
.about-title h2 span{color:var(--gold)}
.about-text p{font-size:13px;line-height:1.6;color:var(--muted);margin-bottom:12px}
.about-text a{font-size:12px;color:var(--gold);text-decoration:none}
.video{width:360px;height:210px;position:relative;background:linear-gradient(135deg,#3b3b3b,#121212 60%,#2b2b2b)}
.video-bar{position:absolute;left:0;right:0;bottom:0;height:28px;background:rgba(0,0,0,.75);display:flex;align-items:center;gap:10px;padding:0 10px}
.video-bar .track{flex:1;height:4px;background:#555;position:relative}
.video-bar .track i{position:absolute;left:0;top:0;height:4px;width:30%;background:var(--gold)}

/* testimonials */
.testimonials{position:relative;height:470px;background:linear-gradient(100deg,#7d5e44 0%,#a98562 35%,#c7ab86 60%,#8f6e50 100%);text-align:center;color:var(--white)}
.testimonials::before{content:"";position:absolute;inset:0;background:rgba(40,28,18,.35)}
.testimonials-inner{position:relative;padding-top:40px}
.testimonials h2{font-size:26px;font-weight:700;text-transform:uppercase;margin-bottom:14px}
.avatar{width:104px;height:104px;border-radius:50%;margin:0 auto 10px;border:4px solid var(--white);background:linear-gradient(160deg,#d8bba0,#8d6b55)}
.client-name{font-size:16px;font-weight:700;margin-bottom:16px}
.testimonials blockquote{width:820px;margin:0 auto;font-size:13px;line-height:1.6}
.t-dots{display:flex;justify-content:center;gap:8px;margin-top:22px}
.t-dots span{width:12px;height:12px;border-radius:50%;background:rgba(255,255,255,.55)}
.t-dots span.on{background:var(--white)}

/* cta banner */
.cta{margin:30px 120px 0;height:70px;background:linear-gradient(180deg,var(--gold-light),var(--gold));display:flex;align-items:center;justify-content:space-between;padding:0 30px;color:var(--white)}
.cta p{font-size:34px;font-style:italic;font-weight:800}
.cta strong{font-size:34px;font-weight:800;display:flex;align-items:center;gap:12px}

/* partners */
.partners{display:flex;justify-content:space-between;padding:16px 120px 0;height:170px}
.partner-group{display:flex;gap:18px;border:1px solid var(--line);padding:14px 18px;height:130px;align-items:center}
.badge{width:116px;height:96px;background:#eee}
.badge.round{border-radius:50%;width:96px}

/* footer */
.footer-nav{position:absolute;left:0;top:2432px;width:1200px;height:34px;background:var(--gold);display:flex;justify-content:center;align-items:center}
.footer-nav a{color:var(--white);font-size:11px;text-decoration:none;padding:0 12px;border-right:1px solid rgba(255,255,255,.5)}
.footer-nav a:last-child{border-right:0}
.footer-bar{position:absolute;left:0;top:2466px;width:1200px;height:46px;background:var(--footer);display:flex;align-items:center;justify-content:space-between;padding:0 100px;color:#bbb;font-size:11px}
.social{display:flex;gap:8px}
.social span{width:20px;height:20px;border-radius:50%;background:var(--gold)}
.payments{display:flex;gap:6px}
.payments span{width:34px;height:22px;background:#555;border-radius:2px}
</style>
</head>
<body>

<header class="site-header">
  <div class="brand"><span class="brand-dot"></span><span class="brand-name">Harwickden Relocation Services</span></div>
  <div class="header-call">
    <small>CALL US TODAY</small>
    <strong><svg width="18" height="18" viewBox="0 0 24 24"><path fill="#2a2a2a" d="M6.6 10.8c1.4 2.8 3.8 5.1 6.6 6.6l2.2-2.2c.3-.3.7-.4 1-.2 1.1.4 2.3.6 3.6.6.6 0 1 .4 1 1V20c0 .6-.4 1-1 1C10.6 21 3 13.4 3 4c0-.6.4-1 1-1h3.5c.6 0 1 .4 1 1 0 1.3.2 2.5.6 3.6.1.3 0 .7-.2 1z"/></svg>(800) 555-0148</strong>
  </div>
</header>

<nav class="main-nav">
  <a class="active" href="#">Household Moves</a>
  <a href="#">Corporate Moves</a>
  <a href="#">Military Moves</a>
  <a href="#">Auto Transport</a>
  <a href="#">About Us</a>
  <a href="#">Testimonials</a>
  <a href="#">Contact Us</a>
</nav>

<section class="hero">
  <div class="hero-photo" role="img" aria-label="Photo of a couple looking out a window in a new home among moving boxes"></div>
  <div class="hero-box">
    <h1>For All Your Long Distance Moving Needs</h1>
    <p>Moving long distance? Harwickden Relocation Services is here to help! From long distance moves to corporate relocation &amp; car transports, we offer professional full-service moves that get you from origin to destination worry free.</p>
    <a class="btn" href="#">Get a Free Estimate &amp; Moving Tips</a>
  </div>
  <div class="hero-dots"><span class="on"></span><span></span><span></span><span></span></div>
</section>

<section class="services">
  <article class="service-card">
    <div class="service-img" role="img" aria-label="Illustration of a moving truck on a road" style="background:linear-gradient(135deg,#7fb0e0,#4a7fb8 55%,#9fc36a)"></div>
    <div>
      <h2>Long Distance Moves</h2>
      <p>Moving long distance can be stressful, but with our team it doesn't have to be. Whether you're crossing state lines or moving clear across the country.</p>
    </div>
  </article>
  <article class="service-card reverse">
    <div class="service-img" role="img" aria-label="Photo of packed moving boxes" style="background:linear-gradient(135deg,#d8b98a,#a9804f)"></div>
    <div>
      <h2>Full-Service Moves</h2>
      <p>Not only will our crew coordinate every detail of your long distance move, we also offer full-service options that will save time and money.</p>
    </div>
  </article>
</section>

<section class="quote">
  <h2>Request a Free Moving Quote</h2>
  <div class="quote-divider"></div>
  <p class="quote-lead">Enter your info and receive a coupon code for your upcoming move...</p>
  <form class="quote-form">
    <div>
      <div class="field"><label>Name</label><div class="input"></div></div>
      <div class="field"><label>Email</label><div class="input"></div></div>
      <div class="field"><label>Mobile</label><div class="input"></div></div>
      <div class="field"><label>Moving from zip</label><div class="input"></div></div>
    </div>
    <div>
      <div class="field"><label>Moving to zip</label><div class="input"></div></div>
      <div class="field"><label>Move type</label><div class="select"><span>Residential</span><span>&#9662;</span></div></div>
      <a class="btn" href="#">Submit</a>
    </div>
  </form>
</section>

<section class="about">
  <div class="about-text">
    <div class="about-title"><span class="mark"></span><h2><span>About</span> Harwickden Relocation Services</h2></div>
    <p>As a licensed, bonded, and insured moving service provider, our team has forged strong relationships with the most TRUSTED and nationally recognized interstate movers and auto transporters in the industry. Due to the volume and quality of our business, our movers treat your move with the highest level of customer satisfaction, and offer discounted rates that are difficult to compete with.</p>
    <a href="#">Read More &rsaquo;</a>
  </div>
  <div class="video" role="img" aria-label="Company introduction video with staff in an office">
    <div class="video-bar">
      <svg width="12" height="12" viewBox="0 0 12 12"><path d="M2 1l9 5-9 5z" fill="#fff"/></svg>
      <div class="track"><i></i></div>
      <svg width="14" height="12" viewBox="0 0 14 12"><path d="M1 4h3l4-3v10L4 8H1z" fill="#fff"/></svg>
    </div>
  </div>
</section>

<section class="testimonials">
  <div role="img" aria-label="Photo of a happy couple sitting among moving boxes" style="position:absolute;inset:0"></div>
  <div class="testimonials-inner">
    <h2>Client Testimonials</h2>
    <div class="avatar" role="img" aria-label="Client portrait"></div>
    <p class="client-name">Lorem Ipsum</p>
    <blockquote>Our move from Ohio to Arizona went perfectly. The crew arrived on time, wrapped every piece of furniture with care and delivered everything a day early. The quote was clear from the start and there were no surprise fees at the end. We would gladly recommend this team to any family planning a long distance move.</blockquote>
    <div class="t-dots"><span class="on"></span><span></span><span></span></div>
  </div>
</section>

<section class="cta">
  <p>Contact us today for a free quote!</p>
  <strong><svg width="30" height="30" viewBox="0 0 24 24"><path fill="#fff" d="M6.6 10.8c1.4 2.8 3.8 5.1 6.6 6.6l2.2-2.2c.3-.3.7-.4 1-.2 1.1.4 2.3.6 3.6.6.6 0 1 .4 1 1V20c0 .6-.4 1-1 1C10.6 21 3 13.4 3 4c0-.6.4-1 1-1h3.5c.6 0 1 .4 1 1 0 1.3.2 2.5.6 3.6.1.3 0 .7-.2 1z"/></svg>(800) 555-0148</strong>
</section>

<section class="partners">
  <div class="partner-group">
    <div class="badge" aria-label="Partner badge"></div>
    <div class="badge" aria-label="Partner badge"></div>
    <div class="badge" aria-label="Partner badge"></div>
  </div>
  <div class="partner-group">
    <div class="badge round" aria-label="Accreditation badge"></div>
    <div class="badge round" aria-label="Accreditation badge"></div>
  </div>
</section>

<nav class="footer-nav">
  <a href="#">Household Moves</a>
  <a href="#">Corporate Moves</a>
  <a href="#">Military Moves</a>
  <a href="#">Auto Transport</a>
  <a href="#">About Us</a>
  <a href="#">Testimonials</a>
  <a href="#">Contact Us</a>
</nav>

<footer class="footer-bar">
  <span>&copy; 2015 Harwickden Relocation Services. All Rights Reserved.</span>
  <div class="social"><span></span><span></span><span></span><span></span><span></span></div>
  <div class="payments"><span></span><span></span><span></span><span></span></div>
</footer>

</body>
</html>
```